Website design for an Italian restaurant in Amsterdam

I need a design for a client of mine. It is for Teatro Lunaverde, an Italian restaurant in Amsterdam.
We are going for a clean, modern look but we also need to realise an authentic feel.
The restaurant is located in an old movie theatre, that is where the name Teatro Lunaverde comes from.
Industry/Entity Type
Italian Restaurant
Number of Pages Required
1 page
Font styles to use
Sans Serif
Colors
Designer to choose colors to be used in the design.

```html
<!DOCTYPE html>
<html lang="en">
<head>
<meta charset="utf-8">
<title>Teatro Lunaverde – Italian Restaurant Amsterdam</title>
<link href="https://fonts.googleapis.com/css2?family=Montserrat:wght@400;500;600;700&family=Niconne&display=swap" rel="stylesheet">
<style>
:root{
  --red:#d3200f;
  --green:#5a9447;
  --green-dark:#4b8139;
  --cream:#f4f2ec;
  --cream-2:#f0eee7;
  --white:#ffffff;
  --ink:#444444;
  --muted:#777777;
  --script:'Niconne', cursive;
  --sans:'Montserrat', sans-serif;
}
*{box-sizing:border-box;margin:0;padding:0}
html,body{width:1200px;height:3220px;overflow:hidden}
body{position:relative;font-family:var(--sans);color:var(--ink);background:var(--cream)}
.section{position:absolute;left:0;width:1200px}
.script{font-family:var(--script);font-weight:400}
.photo{position:absolute}

/* hero */
.hero{top:0;height:640px;background:linear-gradient(100deg,#9a5326 0%,#c17a3f 40%,#a85a28 100%)}
.hero .photo-pizza{left:540px;top:0;width:660px;height:640px;background:radial-gradient(circle at 55% 40%,#e9c27a 0%,#d9953e 35%,#b5541f 60%,rgba(181,84,31,0) 72%)}
.topbar-social{position:absolute;right:152px;top:4px;display:flex;gap:6px}
.topbar-social span{width:10px;height:10px;border-radius:50%;background:var(--white);opacity:.9}
.navbar{position:absolute;left:150px;top:22px;width:902px;height:68px;background:var(--white);display:flex;align-items:center;padding:0 24px;box-shadow:0 2px 6px rgba(0,0,0,.15)}
.brand{font-family:var(--script);font-size:34px;color:var(--ink);margin-right:30px;white-space:nowrap}
.nav{display:flex;list-style:none;font-size:12px;font-weight:500;color:#333;white-space:nowrap}
.nav li{padding:0 12px;border-right:1px solid #bbb;line-height:14px;white-space:nowrap}
.nav-search{margin-left:14px;flex:none}
.hero-title{position:absolute;left:150px;top:240px;width:434px;height:72px;background:var(--red);color:var(--white);font-family:var(--script);font-size:42px;font-weight:400;line-height:72px;padding-left:24px;white-space:nowrap}
.hero-text{position:absolute;left:150px;top:316px;width:434px;height:66px;background:var(--green);color:var(--white);font-size:14px;line-height:22px;padding:10px 20px}
.hero-btn{position:absolute;left:150px;top:404px;width:138px;height:34px;background:var(--red);color:var(--white);font-size:15px;line-height:34px;text-align:center}
.slide-arrow{position:absolute;top:318px;width:24px;height:24px;border-radius:50%;background:rgba(0,0,0,.55)}
.slide-arrow.left{left:14px}.slide-arrow.right{right:12px}
.slide-arrow svg{display:block}

/* headings */
.heading{text-align:center;color:var(--red);font-size:50px;line-height:1;white-space:nowrap}
.divider{position:absolute;height:1px;background:#b9b3a2}
.divider-mark{position:absolute;width:16px;height:16px;border:2px solid var(--green);border-radius:50%;background:var(--cream)}

/* menu */
.menu{top:640px;height:712px;background:var(--cream)}
.menu .heading{position:absolute;top:30px;width:100%}
.dish{position:absolute;width:288px;height:234px}
.dish .photo{left:0;top:0;width:288px;height:191px}
.dish-label{position:absolute;left:0;top:191px;width:288px;height:43px;background:var(--red);color:var(--white);font-family:var(--script);font-size:22px;line-height:43px;text-align:center}

/* about */
.about{top:1352px;height:531px;background:var(--cream-2)}
.about-panel{position:absolute;left:133px;top:18px;width:941px;height:512px;background:var(--white)}
.about h2{color:var(--red);font-size:36px;line-height:44px;text-align:center;width:450px;position:absolute;left:17px;white-space:nowrap}
.about p{position:absolute;left:17px;width:450px;font-size:11.2px;line-height:17px;color:var(--muted)}
.about .photo-room{left:485px;top:30px;width:443px;height:442px;background:linear-gradient(160deg,#3a2a1c 0%,#7a4c22 40%,#c6703a 65%,#8e2a22 100%);border:4px solid #ddd}
.dots{position:absolute;left:670px;top:483px;display:flex;gap:12px}
.dots span{width:6px;height:6px;border-radius:50%;background:#555}

/* features */
.features{top:1883px;height:464px;background:var(--cream)}
.features .heading{position:absolute;top:28px;width:100%}
.feature{position:absolute;top:129px;height:260px;background:var(--green);color:var(--white);text-align:center;padding-top:18px}
.feature svg{display:block;margin:0 auto}
.feature h3{font-family:var(--script);font-size:16px;font-weight:400;margin-top:14px}
.feature p{font-size:11px;font-weight:600;line-height:16px;padding:6px 18px 0}

/* social band */
.social-band{top:2347px;height:240px;background:linear-gradient(90deg,#d9a36a 0%,#efe0c0 30%,#f4e9cf 55%,#e9c89a 80%,#c98a5a 100%)}
.social-list{position:absolute;left:364px;top:117px;display:flex;gap:10px}
.social-list span{width:46px;height:46px;border-radius:50%;background:var(--red);border:2px solid var(--white)}
.to-top{position:absolute;right:8px;bottom:8px;width:24px;height:24px;border-radius:50%;background:var(--green)}

/* cta */
.cta{top:2587px;height:260px;background:var(--cream)}
.cta .heading{position:absolute;top:60px;width:100%;font-size:46px}
.cta-btn{position:absolute;left:500px;top:140px;width:200px;height:49px;background:var(--red);color:var(--white);font-size:18px;line-height:49px;text-align:center}

/* footer */
.footer{top:2847px;height:326px;background:var(--green);color:var(--white)}
.footer h4{position:absolute;font-family:var(--script);font-weight:400;font-size:40px;line-height:48px;white-space:nowrap}
.footer p{position:absolute;font-size:12px;line-height:22px}
.footer-links{position:absolute;left:558px;top:118px;list-style:none;font-size:12.5px;font-weight:600;line-height:28.5px}
.footer-input{position:absolute;left:777px;top:191px;width:284px;height:36px;background:var(--green-dark);font-size:11px;line-height:36px;padding-left:16px;color:#cfe3c6}
.footer-btn{position:absolute;left:777px;top:243px;width:107px;height:34px;background:var(--green-dark);font-size:11px;font-weight:600;line-height:34px;text-align:center}
.bottombar{top:3173px;height:47px;background:var(--green-dark);color:var(--white);font-size:11px;line-height:47px}
.bottombar .copy{position:absolute;left:150px}
.bottombar .links{position:absolute;right:150px;top:18px;display:flex;gap:18px}
.bottombar .links span{width:11px;height:11px;border-radius:50%;background:var(--white)}
</style>
</head>
<body>

<header class="section hero">
  <div class="photo photo-pizza" role="img" aria-label="Photo of a wood-fired pizza with basil, olives and tomatoes on a wooden table"></div>
  <div class="topbar-social" aria-label="Social links"><span></span><span></span><span></span><span></span><span></span></div>
  <nav class="navbar">
    <div class="brand">Teatro Lunaverde</div>
    <ul class="nav">
      <li>Home</li><li>About</li><li>Cuisine &amp; Menu</li><li>Reservation</li><li>Gallery</li><li>Blog</li><li>Contacts</li>
    </ul>
    <svg class="nav-search" width="14" height="14" viewBox="0 0 14 14"><circle cx="6" cy="6" r="4.5" fill="none" stroke="#333" stroke-width="1.6"/><line x1="9.3" y1="9.3" x2="13" y2="13" stroke="#333" stroke-width="1.6"/></svg>
  </nav>
  <div class="slide-arrow left"><svg width="24" height="24"><path d="M14 7 L9 12 L14 17" fill="none" stroke="#fff" stroke-width="2"/></svg></div>
  <div class="slide-arrow right"><svg width="24" height="24"><path d="M10 7 L15 12 L10 17" fill="none" stroke="#fff" stroke-width="2"/></svg></div>
  <h1 class="hero-title">Authentic Italian Cuisine</h1>
  <p class="hero-text">Lorem ipsum dolor sit amet, consectetur adipiscing elit. Suspendisse dolor magna, hendrerit eu lobortis eu.</p>
  <div class="hero-btn">Know more</div>
</header>

<section class="section menu">
  <h2 class="heading script">Our Delicious Menu</h2>
  <div class="divider" style="left:150px;top:97px;width:430px"></div>
  <div class="divider-mark" style="left:592px;top:89px"></div>
  <div class="divider" style="left:620px;top:97px;width:443px"></div>

  <div class="dish" style="left:150px;top:144px"><div class="photo" role="img" aria-label="Photo of pasta with mussels" style="background:linear-gradient(135deg,#e8d2a8,#b5651f 60%,#3b2a20)"></div><div class="dish-label">Macaroni</div></div>
  <div class="dish" style="left:464px;top:144px"><div class="photo" role="img" aria-label="Photo of lasagne with basil" style="background:linear-gradient(135deg,#6c5a3e,#c9762e 50%,#e9e4d8)"></div><div class="dish-label">Lasagne</div></div>
  <div class="dish" style="left:775px;top:144px"><div class="photo" role="img" aria-label="Photo of pizza slices" style="background:linear-gradient(135deg,#d9b06c,#a9672b 55%,#6a8a3a)"></div><div class="dish-label">Pizza</div></div>
  <div class="dish" style="left:150px;top:410px"><div class="photo" role="img" aria-label="Photo of a panini sandwich" style="background:linear-gradient(135deg,#b3281e,#e4cfa6 50%,#7a9a3a)"></div><div class="dish-label">Panini</div></div>
  <div class="dish" style="left:464px;top:410px"><div class="photo" role="img" aria-label="Photo of fried arancini balls" style="background:linear-gradient(135deg,#5a3b2a,#e3b14a 50%,#f3efe4)"></div><div class="dish-label">Arancini</div></div>
  <div class="dish" style="left:775px;top:410px"><div class="photo" role="img" aria-label="Photo of an antipasti platter" style="background:linear-gradient(135deg,#3c2b1f,#b14a35 50%,#c9a56b)"></div><div class="dish-label">Antipasti</div></div>
</section>

<section class="section about">
  <div class="about-panel">
    <h2 class="script" style="top:38px">A Piece of Teatro Lunaverde</h2>
    <div class="divider" style="left:85px;top:92px;width:138px"></div>
    <div class="divider-mark" style="left:234px;top:84px;background:#fff"></div>
    <div class="divider" style="left:262px;top:92px;width:138px"></div>
    <p style="top:106px">Lorem ipsum dolor sit amet, consectetur adipiscing elit. Ut elit tellus, luctus nec ullamcorper mattis, pulvinar dapibus leo. elit tellus, luctus nec ullamcorper mattis, pulvinar dapibus leo. Lorem ipsum dolor sit amet, consectetur adipiscing elit. Ut elit tellus, luctus nec ullamcorper mattis, pulvinar dapibus leo. elit tellus, luctus nec ullamcorper mattis, pulvinar dapibus leo.</p>
    <p style="top:208px">Lorem ipsum dolor sit amet, consectetur adipiscing elit. Ut elit tellus, luctus nec ullamcorper mattis, pulvinar dapibus leo. elit tellus, luctus nec ullamcorper mattis, pulvinar dapibus leo. Lorem ipsum dolor sit amet, consectetur adipiscing elit. Ut elit tellus, luctus nec ullamcorper mattis, pulvinar dapibus leo. elit tellus, luctus nec ullamcorper mattis, pulvinar dapibus leo. read more</p>
    <h2 class="script" style="top:318px">Authentic Italian Cuisine</h2>
    <p style="top:362px">Lorem ipsum dolor sit amet, consectetur adipiscing elit. Ut elit tellus, luctus nec ullamcorper mattis, pulvinar dapibus leo. elit tellus, luctus nec ullamcorper mattis, pulvinar dapibus leo. Lorem ipsum dolor sit amet, consectetur adipiscing elit. Ut elit tellus, luctus nec ullamcorper mattis, pulvinar dapibus leo. read more</p>
    <div class="photo photo-room" role="img" aria-label="Photo of the restaurant dining room with red tablecloths and wooden chairs"></div>
    <div class="dots"><span></span><span></span><span style="background:none;border:1px solid #555"></span><span></span></div>
  </div>
</section>

<section class="section features">
  <h2 class="heading script">Good Food...Good Mood</h2>
  <div class="feature" style="left:150px;width:204px">
    <svg width="60" height="60" viewBox="0 0 60 60" fill="none" stroke="#fff" stroke-width="2"><path d="M10 52 L38 24 L44 30 Z"/><path d="M40 22 L50 10 M42 24 L54 18 M38 20 L40 8"/></svg>
    <h3>Organic Ingredients</h3>
    <p>Lorem ipsum dolor sit amet, sit copiosae interesset ut. Vim dicant dolorum perpetua in, magna putant te lus. Mucius atomorum pro an, dolor sit amet, sit copiosae interesset ut.</p>
  </div>
  <div class="feature" style="left:384px;width:206px">
    <svg width="60" height="60" viewBox="0 0 60 60" fill="none" stroke="#fff" stroke-width="2"><path d="M8 32 H52 C52 44 42 52 30 52 C18 52 8 44 8 32 Z"/><path d="M18 32 C18 20 26 14 34 18 M30 32 C32 24 40 20 46 24"/></svg>
    <h3>Freshly Cooked</h3>
    <p>Lorem ipsum dolor sit amet, sit copiosae interesset ut. Vim dicant dolorum perpetua in, magna putant te lus. Mucius atomorum pro an, dolor sit amet, sit copiosae interesset ut.</p>
  </div>
  <div class="feature" style="left:618px;width:204px">
    <svg width="60" height="60" viewBox="0 0 60 60" fill="none" stroke="#fff" stroke-width="2"><path d="M18 34 C8 32 8 16 20 18 C22 8 38 8 40 18 C52 16 52 32 42 34 V48 H18 Z"/><line x1="18" y1="42" x2="42" y2="42"/></svg>
    <h3>Home Made</h3>
    <p>Lorem ipsum dolor sit amet, sit copiosae interesset ut. Vim dicant dolorum perpetua in, magna putant te lus. Mucius atomorum pro an, dolor sit amet, sit copiosae interesset ut.</p>
  </div>
  <div class="feature" style="left:852px;width:208px">
    <svg width="60" height="60" viewBox="0 0 60 60" fill="none" stroke="#fff" stroke-width="2"><path d="M18 8 H42 V22 C42 30 36 34 30 34 C24 34 18 30 18 22 Z"/><line x1="30" y1="34" x2="30" y2="50"/><line x1="20" y1="52" x2="40" y2="52"/><line x1="18" y1="18" x2="42" y2="18"/></svg>
    <h3>Free Champaign</h3>
    <p>Lorem ipsum dolor sit amet, sit copiosae interesset ut. Vim dicant dolorum perpetua in, magna putant te lus. Mucius atomorum pro an, dolor sit amet, sit copiosae interesset ut.</p>
  </div>
</section>

<section class="section social-band" role="img" aria-label="Photo of assorted colourful dry pasta shapes">
  <div class="social-list" aria-label="Social links"><span></span><span></span><span></span><span></span><span></span><span></span><span></span><span></span><span></span></div>
  <div class="to-top"><svg width="24" height="24"><path d="M8 14 L12 10 L16 14" fill="none" stroke="#fff" stroke-width="2"/></svg></div>
</section>

<section class="section cta">
  <h2 class="heading script">Italian Taste Delivered to your Doorstep</h2>
  <div class="cta-btn">Order Online Now</div>
</section>

<footer class="section footer">
  <h4 style="left:150px;top:58px">Teatro Lunaverde</h4>
  <p style="left:150px;top:112px;width:350px">Lorem ipsum dolor sit amet, consectetur adipiscing elit. Suspendisse dolor magna, hendrerit eu lobortis eu, tincidunt in quam. Phasellus in lectus non lacus imper diet pellentesque. Duis diam leo, mattis non risus nec, malesuada dictum neque. Phasellus eu viverra lectus. Mauris ultrices tortor lobortis luctus fermentum. Sed dignissim lectus sed consectetur tincidunt.</p>
  <h4 style="left:541px;top:52px">Quick Links</h4>
  <ul class="footer-links"><li>About</li><li>Cruisine &amp; Menu</li><li>Reservation</li><li>Gallery</li><li>Blog</li><li>Contacts</li></ul>
  <h4 style="left:766px;top:52px">Mailing List</h4>
  <p style="left:777px;top:112px;width:290px">Lorem ipsum dolor sit amet, consectetur adipiscing elit. Suspendisse dolor magna, hendrerit eu lobortis eu, tincidunt in quam.</p>
  <div class="footer-input">Your email</div>
  <div class="footer-btn">JOIN NOW</div>
</footer>

<div class="section bottombar">
  <span class="copy">Copyright © Teatro Lunaverde 2018. All rights reserved.</span>
  <div class="links" aria-label="Social links"><span></span><span></span><span></span><span></span></div>
</div>

</body>
</html>
```